Product Label Design

Need a product design for our Epsom salt product, needs to have a luxurious simple feel to it. The picture attached is our brand and wordage on it, the bag we think should be a stand up bag that should be offwhite/creme color. The other picture are products that we like. We updated the packaging to be a Kraft tube box, please see the attached photo for dimensions.

```html
<!DOCTYPE html>
<html lang="en">
<head>
<meta charset="utf-8">
<title>Navo Brighten — Epsom Salt Label</title>
<link href="https://fonts.googleapis.com/css2?family=Archivo:wght@700;800;900&display=swap" rel="stylesheet">
<style>
  :root {
    --label-bg: #ffffff;
    --brand-navy: #0a425e;
    --ink: #000000;
  }
  html, body {
    margin: 0;
    padding: 0;
    overflow: hidden;
    background: var(--label-bg);
  }
  .label {
    position: relative;
    width: 900px;
    height: 1200px;
    background: var(--label-bg);
    font-family: "Archivo", "Helvetica Neue", Arial, sans-serif;
    overflow: hidden;
  }
  .brand-name {
    position: absolute;
    top: 372px;
    left: 0;
    width: 900px;
    text-align: center;
    margin: 0;
    font-size: 160px;
    font-weight: 900;
    line-height: 1;
    letter-spacing: -6px;
    color: var(--brand-navy);
  }
  .blend-name {
    position: absolute;
    top: 612px;
    left: 0;
    width: 900px;
    text-align: center;
    margin: 0;
    font-size: 31px;
    font-weight: 800;
    line-height: 40px;
    letter-spacing: 3px;
    color: var(--ink);
  }
  .ingredients {
    position: absolute;
    top: 673px;
    left: 0;
    width: 900px;
    margin: 0;
    padding: 0;
    list-style: none;
    text-align: center;
    font-size: 25px;
    font-weight: 800;
    letter-spacing: 1.6px;
    line-height: 31px;
    color: var(--ink);
  }
  .ingredients li {
    margin: 0;
    padding: 0;
    white-space: pre;
  }
  .ingredients .shift-left { margin-right: 60px; }
  .net-weight {
    position: absolute;
    top: 1108px;
    left: 0;
    width: 900px;
    text-align: center;
    margin: 0;
    font-size: 26px;
    font-weight: 800;
    line-height: 40px;
    letter-spacing: 2.4px;
    color: var(--brand-navy);
  }
</style>
</head>
<body>
  <main class="label">
    <h1 class="brand-name">Navo</h1>
    <h2 class="blend-name">BRIGHTEN</h2>
    <ul class="ingredients"><li>US Sourced Pure Epsom Salt</li><li>(Magnesium Sulfate)</li><li class="shift-left">+   Abies Sibirica</li><li class="shift-left">+   + Fir Balsam</li></ul>
    <p class="net-weight">NET WT. 3LBS (1360g)</p>
  </main>
</body>
</html>
```